Business Card Design

Business Card for professional consulting firm working with large financial institutions.

Target Market(s)

Executive buyers

Industry/Entity Type

Banking

Contact Information for Business Card

Mild creativity wanted. Not boring, but do elaborate artwork.

Font styles to use
Serif
Sans Serif

Colors

Designer to choose colors to be used in the design.

Requirements
Must have
• Standard business card features - company name, individual name, telephone, website, email, locations.
Nice to have
• Two colors
Should not have
• too many colors, fancy printing, cartoons.

```html
<!DOCTYPE html>
<html lang="en">
<head>
<meta charset="utf-8">
<title>Halverton business cards</title>
<link href="https://fonts.googleapis.com/css2?family=Open+Sans:wght@400;600;700&display=swap" rel="stylesheet">
<style>
:root{
  --page:#f2f2f2;
  --card:#ffffff;
  --ink:#1f1f1f;
  --name:#454545;
  --muted:#8a8a8a;
  --bar:#4a4a4a;
  --globe:#e8e8e8;
  --night-a:#2c2a2a;
  --night-b:#3b3533;
  --white:#ffffff;
  --rule:#bdbdbd;
}
*{margin:0;padding:0;box-sizing:border-box}
html,body{width:1200px;height:750px;overflow:hidden}
body{background:var(--page);position:relative;font-family:"Open Sans",Arial,sans-serif;color:var(--ink)}
.card{position:absolute;width:480px;height:274px;overflow:hidden;box-shadow:4px 6px 10px rgba(0,0,0,.35)}
.front{background:var(--card)}
.row-1{top:80px}
.row-2{top:396px}
.col-front{left:108px}
.col-back{left:610px}

.brand{position:absolute;right:38px;top:27px;font-family:"Open Sans",Arial,sans-serif;font-weight:400;font-size:27px;color:var(--name);line-height:1;letter-spacing:.3px}

.name-bar{position:absolute;left:0;top:82px;width:17px;height:46px;background:var(--bar)}
.person{position:absolute;left:25px;top:83px}
.person-name{font-size:21px;font-weight:700;color:var(--name);letter-spacing:.2px;line-height:1.15}
.person-title{font-size:15px;color:var(--muted);line-height:1.3}

.globe{position:absolute;width:300px;height:300px;border-radius:50%;background:var(--globe)}
.globe-left{left:-30px;top:155px}
.globe-right{left:235px;top:118px}

.details{position:absolute;top:157px;width:230px}
.details-right{left:263px}
.details-left{left:25px}
.address{font-size:11px;font-weight:600;line-height:14px;color:var(--ink);margin-bottom:9px}
.contact{list-style:none}
.contact li{display:flex;align-items:center;font-size:13px;line-height:19px;color:var(--name)}
.contact svg{width:10px;height:10px;margin-right:6px;flex:none;fill:var(--name)}

.back{background:linear-gradient(160deg,var(--night-a),var(--night-b) 55%,var(--night-a))}
.back-brand{position:absolute;left:0;right:0;top:121px;text-align:center;font-family:"Open Sans",Arial,sans-serif;font-weight:400;font-size:36px;color:var(--white);line-height:1;letter-spacing:.5px}
.back-web{position:absolute;left:0;right:0;top:244px;display:flex;align-items:center;gap:10px;font-size:12.5px;font-weight:600;color:var(--white)}
.back-web::before{content:"";height:1px;background:var(--rule);flex:0 0 170px}
.back-web::after{content:"";height:1px;background:var(--rule);flex:1}
</style>
</head>
<body>

<section class="card front row-1 col-front">
  <div class="globe globe-left" role="img" aria-label="Faint grey globe illustration"></div>
  <div class="brand">Halverton</div>
  <div class="name-bar"></div>
  <div class="person">
    <div class="person-name">DANA WHITCOMBE</div>
    <div class="person-title">Founder &amp; Managing Partner</div>
  </div>
  <div class="details details-right">
    <p class="address">410 W Meridian Avenue Harbor Point<br>Tower 12th Floor Tucson<br>Arizona 85701</p>
    <ul class="contact">
      <li><svg viewBox="0 0 10 10"><path d="M3 0h4a1 1 0 0 1 1 1v8a1 1 0 0 1-1 1H3a1 1 0 0 1-1-1V1a1 1 0 0 1 1-1zm0 1.5v6h4v-6z"/></svg>520-555-0148</li>
      <li><svg viewBox="0 0 10 10"><circle cx="5" cy="5" r="5"/></svg>www.halverton.com</li>
      <li><svg viewBox="0 0 10 10"><rect x="0" y="2.5" width="10" height="5"/></svg>info@halverton.com</li>
    </ul>
  </div>
</section>

<section class="card back row-1 col-back" role="img" aria-label="Dark city skyline photograph">
  <div class="back-brand">Halverton</div>
  <div class="back-web">www.halverton.com</div>
</section>

<section class="card front row-2 col-front">
  <div class="globe globe-right" role="img" aria-label="Faint grey globe illustration"></div>
  <div class="brand">Halverton</div>
  <div class="name-bar"></div>
  <div class="person">
    <div class="person-name">DANA WHITCOMBE</div>
    <div class="person-title">Founder &amp; Managing Partner</div>
  </div>
  <div class="details details-left">
    <p class="address">410 W Meridian Avenue Harbor Point<br>Tower 12th Floor Tucson<br>Arizona 85701</p>
    <ul class="contact">
      <li><svg viewBox="0 0 10 10"><path d="M3 0h4a1 1 0 0 1 1 1v8a1 1 0 0 1-1 1H3a1 1 0 0 1-1-1V1a1 1 0 0 1 1-1zm0 1.5v6h4v-6z"/></svg>520-555-0148</li>
      <li><svg viewBox="0 0 10 10"><circle cx="5" cy="5" r="5"/></svg>www.halverton.com</li>
      <li><svg viewBox="0 0 10 10"><rect x="0" y="2.5" width="10" height="5"/></svg>info@halverton.com</li>
    </ul>
  </div>
</section>

<section class="card back row-2 col-back" role="img" aria-label="Dark city skyline photograph">
  <div class="back-brand">Halverton</div>
  <div class="back-web">www.halverton.com</div>
</section>

</body>
</html>
```